Door Hanger for 20% off on dry cleaning

I need a door hanger (3.5" x 8.5" with a hole for the door handle) for a 20% off sale on dry cleaning. The business is called "Suds on Maple" and is a full-service laundry. The store is a laundromat that is used by self-serve customers. We also do wash-and-fold laundry and dry cleaning.

Some requirements:
* Include the logo
* Includes the address of the business:
215 South 600 West
Provo, Utah
(behind Golden Crust Bakery)
* Include some indication of our other services (wash-and-fold laundry, coin laundry, comforters cleaned)
* Offer needs to include an expiration date (say, September 30, 2014).

The door hanger should be full-color with designs for both sides.
Updates

The sale is for 20% off of Dry Cleaning - not the other services. And I'd like both sides of the hanger to mention the sale - in case it gets hung backwards on the door.

Industry/Entity Type

Dry Cleaning

```html
<!DOCTYPE html>
<html lang="en">
<head>
<meta charset="utf-8">
<title>Suds on Maple – Door Hanger</title>
<link rel="stylesheet" href="https://fonts.googleapis.com/css2?family=Archivo+Black&family=Arimo:wght@400;700&display=swap">
<style>
  :root {
    --page-bg: #e9e6df;
    --navy: #1d2f93;
    --royal: #2a4bc4;
    --orange: #ef5a2a;
    --white: #ffffff;
    --info-bg: #b9defa;
    --sky-top: #2f6fd0;
    --sky-mid: #8cc2ef;
    --horizon: #d8ecf8;
    --grass-top: #6fb43a;
    --grass-bottom: #2f7a1e;
  }
  html, body {
    margin: 0;
    width: 1200px;
    height: 1200px;
    overflow: hidden;
    background: var(--page-bg);
  }
  .canvas {
    position: relative;
    width: 1200px;
    height: 1200px;
  }
  .door-hanger {
    position: absolute;
    left: 380px;
    top: 66px;
    width: 440px;
    height: 1068px;
    overflow: hidden;
    font-family: "Arimo", Arial, sans-serif;
    box-shadow: 0 2px 10px rgba(0,0,0,0.15);
  }
  .scenery {
    position: absolute;
    inset: 0;
    background: linear-gradient(to bottom,
      var(--sky-top) 0%,
      var(--sky-mid) 35%,
      var(--horizon) 68%,
      var(--grass-top) 71%,
      var(--grass-bottom) 100%);
  }
  .handle-hole {
    position: absolute;
    left: 120px;
    top: 92px;
    width: 198px;
    height: 198px;
    border-radius: 50%;
    background: var(--page-bg);
  }
  .handle-slit {
    position: absolute;
    left: 217px;
    top: 0;
    width: 4px;
    height: 96px;
    background: var(--page-bg);
  }
  .brand {
    position: absolute;
    left: 14px;
    top: 362px;
    display: flex;
    align-items: center;
    gap: 14px;
    white-space: nowrap;
  }
  .brand-mark {
    width: 64px;
    height: 64px;
    background: var(--royal);
  }
  .brand-name {
    font-weight: 700;
    font-size: 40px;
    color: var(--navy);
    line-height: 1;
  }
  .headline {
    position: absolute;
    left: 30px;
    top: 492px;
    width: 400px;
    color: var(--navy);
    font-weight: 700;
    text-transform: uppercase;
  }
  .headline-full {
    font-size: 45px;
    line-height: 1;
    letter-spacing: -0.5px;
    padding-left: 4px;
  }
  .headline-full sup {
    font-size: 30px;
    color: var(--white);
    vertical-align: 18px;
  }
  .headline-rest {
    display: flex;
    align-items: center;
    margin-top: -4px;
  }
  .ampersand {
    font-family: "Archivo Black", "Arial Black", sans-serif;
    font-size: 88px;
    line-height: 0.9;
    color: var(--royal);
    margin-right: 4px;
  }
  .headline-stack { line-height: 1; }
  .headline-self { font-size: 45px; letter-spacing: -0.5px; }
  .headline-mat { font-size: 38px; font-weight: 400; letter-spacing: 0.5px; }
  .coupon {
    position: absolute;
    left: 27px;
    top: 646px;
    width: 385px;
    height: 167px;
    background: var(--orange);
    border-radius: 12px;
    box-sizing: border-box;
    padding: 8px;
  }
  .coupon-inner {
    position: relative;
    height: 100%;
    border: 2px dashed var(--white);
    border-radius: 8px;
    box-sizing: border-box;
    color: var(--white);
  }
  .coupon-amount {
    position: absolute;
    left: 12px;
    top: 6px;
    font-family: "Archivo Black", "Arial Black", sans-serif;
    font-size: 64px;
    line-height: 1;
    text-shadow: 2px 2px 0 var(--navy);
  }
  .coupon-bang {
    position: absolute;
    right: 14px;
    top: 0;
    font-family: "Archivo Black", "Arial Black", sans-serif;
    font-size: 108px;
    line-height: 1;
    text-shadow: 2px 2px 0 var(--navy);
  }
  .coupon-item {
    position: absolute;
    left: 12px;
    top: 80px;
    font-family: "Archivo Black", "Arial Black", sans-serif;
    font-size: 26px;
    letter-spacing: 1px;
  }
  .coupon-expiry {
    position: absolute;
    left: 0;
    right: 0;
    bottom: 10px;
    text-align: center;
    font-size: 15px;
    font-weight: 700;
  }
  .services {
    position: absolute;
    top: 838px;
    left: 40px;
    width: 370px;
    display: flex;
    justify-content: space-between;
    color: var(--white);
    text-transform: uppercase;
  }
  .service-group h3 {
    margin: 0;
    font-size: 17px;
    font-weight: 700;
  }
  .service-group h3 span { font-size: 22px; vertical-align: -2px; }
  .service-group ul {
    margin: 2px 0 0 14px;
    padding: 0;
    list-style: none;
    font-size: 11px;
    font-weight: 700;
    line-height: 1.25;
  }
  .service-group li::before { content: "•"; margin-right: 2px; }
  .self-serve { margin-right: 20px; }
  .location {
    position: absolute;
    left: 27px;
    top: 930px;
    width: 385px;
    height: 100px;
    background: var(--info-bg);
    border-radius: 12px;
    text-align: center;
    text-transform: uppercase;
    box-sizing: border-box;
    padding-top: 10px;
  }
  .location h2 {
    margin: 0;
    font-size: 31px;
    font-weight: 700;
    color: var(--orange);
    line-height: 1.05;
  }
  .location .street {
    margin: 6px 0 0;
    font-size: 19px;
    font-weight: 700;
    color: var(--navy);
  }
  .location .landmark {
    margin: 2px 0 0;
    font-size: 16px;
    color: var(--navy);
  }
</style>
</head>
<body>
<div class="canvas">
  <div class="door-hanger">
    <div class="scenery" role="img" aria-label="Photo of a blue sky with white clouds above a green grass field"></div>
    <div class="handle-slit"></div>
    <div class="handle-hole"></div>

    <div class="brand">
      <div class="brand-mark"></div>
      <div class="brand-name">Suds on Maple</div>
    </div>

    <div class="headline">
      <div class="headline-full">Full-Service<sup>*</sup></div>
      <div class="headline-rest">
        <span class="ampersand">&amp;</span>
        <div class="headline-stack">
          <div class="headline-self">Self-Serve</div>
          <div class="headline-mat">Laundromat</div>
        </div>
      </div>
    </div>

    <div class="coupon">
      <div class="coupon-inner">
        <div class="coupon-amount">20% off</div>
        <div class="coupon-bang">!</div>
        <div class="coupon-item">ON DRY CLEANING</div>
        <div class="coupon-expiry">OFFER EXPIRES: SEPTEMBER 30, 2014.</div>
      </div>
    </div>

    <div class="services">
      <div class="service-group">
        <h3><span>*</span>Full-Service:</h3>
        <ul>
          <li>Wash-and-Fold Laundry</li>
          <li>Dry Cleaning</li>
          <li>Comforters</li>
        </ul>
      </div>
      <div class="service-group self-serve">
        <h3><span>*</span>Self-Serve:</h3>
        <ul>
          <li>Coin Laundry</li>
        </ul>
      </div>
    </div>

    <div class="location">
      <h2>Where are we?</h2>
      <p class="street">215 South 600 West, Provo, Utah</p>
      <p class="landmark">(Behind Golden Crust Bakery)</p>
    </div>
  </div>
</div>
</body>
</html>
```